Online training business needs new website

We need a new wordpress website as a result of a rebranding. The business is a crisis management training company focussed on online training and simulation exercises. We only need a 4 page site - home, about us, contact us and blog. However we must be able to add additional tabs in the header to redirect to our sales and marketing system (Vendolo). As these change from time to time, we must be able to add and delete as required.The site must be editable by us, with a basic understanding of wordpress and no understanding of coding. We don't want to have to employ someone to change text, add posts or add a new workshops etc. The theme chosen must be easy to edit by a beginner.

Target Market(s)

Senior managers food and consumer goods companies

Industry/Entity Type

Consulting

Coding

Coded - Design and coding required

Font styles to use
Sans Serif

Requirements
Must have
• Home page, about us, contact us, blog
• Colour scheme from logo (attached) - maroon, blue and grey
• If you go to the current website "brightfernacademy.com" and click on the "workshops" tab you will see the content I need on the home page for the stormbeacon.com site
Nice to have
• Modern, simple and minimalist design is preferred

```html
<!DOCTYPE html>
<html lang="en">
<head>
<meta charset="utf-8">
<title>Storm Beacon – Crisis Workshops</title>
<link rel="stylesheet" href="https://fonts.googleapis.com/css2?family=Roboto:wght@300;400;500;700&display=swap">
<style>
  :root {
    --maroon: #951a4f;
    --navy: #07507f;
    --white: #ffffff;
    --ink: #1f1f1f;
    --hero-dark: #5d5a55;
    --hero-light: #b3aca2;
  }
  * { box-sizing: border-box; margin: 0; padding: 0; }
  html, body { width: 1200px; height: 2250px; overflow: hidden; }
  body {
    font-family: "Roboto", Arial, sans-serif;
    color: var(--ink);
    background: var(--white);
    position: relative;
  }

  /* Hero */
  .hero { position: absolute; left: 0; top: 0; width: 1200px; height: 753px; color: var(--white); }
  .hero-photo {
    position: absolute; inset: 0;
    background: linear-gradient(160deg, var(--hero-dark) 0%, #8a847b 40%, var(--hero-light) 70%, #77726b 100%);
  }
  .hero-shade { position: absolute; inset: 0; background: rgba(40, 38, 36, 0.35); }
  .brand { position: absolute; left: 78px; top: 72px; display: flex; align-items: center; gap: 14px; }
  .brand-mark { width: 60px; height: 60px; border: 5px solid var(--white); border-radius: 50%; }
  .brand-name { font-size: 34px; font-weight: 500; line-height: 1; letter-spacing: 1px; text-transform: uppercase; }
  .main-nav { position: absolute; right: 68px; top: 106px; display: flex; gap: 37px; }
  .main-nav a { color: var(--white); text-decoration: none; font-size: 37px; font-weight: 400; }
  .hero-title { position: absolute; top: 336px; width: 100%; text-align: center; font-size: 49px; font-weight: 400; }
  .hero-tagline { position: absolute; top: 424px; width: 100%; text-align: center; font-size: 36px; font-weight: 400; line-height: 45px; }
  .scroll-cue { position: absolute; left: 579px; top: 690px; }

  /* Intro band */
  .intro-band {
    position: absolute; top: 753px; left: 0; width: 1200px; height: 179px;
    background: var(--maroon); color: var(--white);
    display: flex; align-items: center; justify-content: center; text-align: center;
    font-size: 40px; font-weight: 400; line-height: 51px;
  }

  /* Risk section */
  .risk { position: absolute; top: 932px; left: 0; width: 1200px; height: 606px; }
  .risk p { font-size: 27px; font-weight: 300; line-height: 35px; }
  .risk-lead { position: absolute; left: 92px; top: 46px; width: 440px; }
  .risk-photo {
    position: absolute; left: 92px; top: 258px; width: 451px; height: 284px;
    background: linear-gradient(135deg, #3c4a55 0%, #7d8a92 45%, #c9c6bf 75%, #2f2a26 100%);
  }
  .risk-facts { position: absolute; left: 646px; top: 46px; width: 470px; }
  .risk-facts p + p { margin-top: 35px; }

  /* Workshops */
  .workshops {
    position: absolute; top: 1538px; left: 0; width: 1200px; height: 400px;
    background: var(--maroon); color: var(--white); text-align: center;
  }
  .workshops h2 { margin-top: 28px; font-size: 37px; font-weight: 400; }
  .workshops .register-note { margin-top: 4px; font-size: 27px; font-weight: 400; }
  .workshop { position: absolute; top: 144px; width: 309px; }
  .workshop.sydney { left: 208px; }
  .workshop.melbourne { left: 672px; }
  .workshop-photo { width: 309px; height: 188px; }
  .sydney .workshop-photo { background: linear-gradient(180deg, #d5dde3 0%, #8fa5b3 40%, #2e8a93 70%, #1c6d78 100%); }
  .melbourne .workshop-photo { background: linear-gradient(180deg, #7fb0d8 0%, #b9cddd 45%, #7e7a74 75%, #4d5a52 100%); }
  .workshop-date { margin-top: 8px; font-size: 21px; font-weight: 400; }

  /* Footer */
  .site-footer { position: absolute; top: 1938px; left: 0; width: 1200px; height: 312px; background: var(--navy); color: var(--white); }
  .footer-col { position: absolute; top: 66px; text-align: center; font-size: 29px; font-weight: 300; line-height: 37px; }
  .footer-col h3 { font-size: 30px; font-weight: 700; }
  .footer-contact { left: 182px; width: 200px; }
  .footer-find { left: 515px; width: 200px; }
  .footer-map { left: 870px; text-align: left; font-weight: 300; }
  .social { position: absolute; left: 870px; top: 218px; display: flex; gap: 18px; }
  .social span { width: 36px; height: 36px; border-radius: 50%; background: var(--white); display: block; }
</style>
</head>
<body>
  <header class="hero">
    <div class="hero-photo" role="img" aria-label="Photo of a team working around a desk with laptops, phones and sketched plans"></div>
    <div class="hero-shade"></div>
    <div class="brand">
      <span class="brand-mark"></span>
      <span class="brand-name">Storm<br>Beacon</span>
    </div>
    <nav class="main-nav">
      <a href="#">Home</a>
      <a href="#">About</a>
      <a href="#">Contact</a>
      <a href="#">Blog</a>
    </nav>
    <h1 class="hero-title">Welcome to Storm Beacon</h1>
    <p class="hero-tagline">protect your brand | reconnect with customers |<br>strengthen your business</p>
    <svg class="scroll-cue" width="42" height="28" viewBox="0 0 42 28" aria-hidden="true">
      <polyline points="5,5 21,21 37,5" fill="none" stroke="#ffffff" stroke-width="8" stroke-linecap="round" stroke-linejoin="round"/>
    </svg>
  </header>

  <section class="intro-band">
    <p>Workshops &amp; simulations to help food and<br>consumer goods companies prevent a crisis</p>
  </section>

  <section class="risk">
    <p class="risk-lead">If you are a food or consumer goods manufacturer, distributor or retailer, a major incident or a product recall can quickly escalate into a crisis!</p>
    <div class="risk-photo" role="img" aria-label="Photo of two business people shaking hands over a desk"></div>
    <div class="risk-facts">
      <p>The average cost of a crisis is $10m and 25% cost over $100m</p>
      <p>Small and medium size businesses often don't survive at all</p>
      <p>The largest cost to any size business is to your reputation &amp; brand - that impacts customer relationships &amp; long term sales!</p>
      <p>Reputation risk remains the number one concern of senior executives, but most are unprepared for a crisis</p>
    </div>
  </section>

  <section class="workshops">
    <h2>NEXT WORKSHOPS</h2>
    <p class="register-note">Click to register</p>
    <a class="workshop sydney">
      <div class="workshop-photo" role="img" aria-label="Photo of Sydney harbour with ferries and the city skyline"></div>
      <p class="workshop-date">Sydney, 28-29 March 2019</p>
    </a>
    <a class="workshop melbourne">
      <div class="workshop-photo" role="img" aria-label="Photo of Melbourne city skyline behind a river bridge"></div>
      <p class="workshop-date">Melbourne, 4-5 April, 2019</p>
    </a>
  </section>

  <footer class="site-footer">
    <div class="footer-col footer-contact">
      <h3>Contact</h3>
      <p>Tel. ********</p>
      <p>Email. ********</p>
    </div>
    <div class="footer-col footer-find">
      <h3>Find us</h3>
      <p>Address</p>
    </div>
    <div class="footer-col footer-map">MAP</div>
    <div class="social" aria-label="Social links">
      <span></span><span></span><span></span><span></span>
    </div>
  </footer>
</body>
</html>
```